Brochure Design- Targeted at Property Developers

We are the largest Conveyancing (property law) firm in the state of Victoria, Australia.

We need a very sophisticated brochure to enable us to take the next step and compete with law firms for property developer clients.

Much about us can be found on our website (inlcuding logos, photos, etc) www.trellowby.com.au but our business name is Trellowby- Marsh Vale not just Trellowby. ALSO I HAVE ATTACHED MANY PHOTOS OF OUR STAFF AND SOME LOGOS TO HELP!!

Size: fold (A3 double sided so that there is 4 A4 pages)

Copy:

This can be played with by the designer to spread across the 4 pages. Ideally the front page will be very minimalistic and not mention our brand (or at least the brand should not dominate):

Page 1: Do property developers have a genuine alternative to high legal fees?

Page 2 and 3:

- 100% of our developer clients recommend us
- We already look after the Conveyancing needs of more developers in Victoria than any other Conveyancing firm
- Industry benchmark off- the- plan contracts (tailored to the requirements of each development). Our special conditions (including variations, rebates and resale restrictions) are carefully chosen to protect the interests of our vendors while being commercially sensitive to ensure sales are not lost unnecessarily
- Expert in guiding developers from first time dual occupancies to seasoned developers of large scale land and highrise projects
- Our large team and highly refined systems ensure fastest possible settlement times after subdivision registration
- We are available to train your project marketers on completing and executing contracts so that sales are not delayed or lost
- Establishment of interest bearing trust accounts
- Before you buy a development site have us thoroughly investigate the contract and vendors statement. We can then conduct the purchase settlement on your behalf.
- We have the friendliest and most efficient staff. Every dealing you have with our dedicated Development Division will be prompt, professional and impressive. You will never need to follow us up!
- Highly experienced Conveyancers with the security of full Solicitor support

Please consider us next time you need Conveyancing.

Services options:
- Use us from contract preparation to settlement or;
- Have your Solicitor prepare the contract and use us as an alternative for the settlement stage only. Many Solicitors recommend us for this service already
- Fast subdivision lodgements (including obtaining mortgagee’s consent, Solicitor preparation of Land Titles Office application, owners corporation establishment)

Page 4: Just our contact details (see our website)

The design should make us look highly professional, conservative, yet cutting edge.

Target Market(s)

Property developers of small to medium sized land and unit developments

Industry/Entity Type

Security

Requirements
Must have
• - Our logo and contact details as well as the copy above.
Nice to have
• - Pictures of land sites, highrise buildings under construction
Should not have
• I really dislike overly corny photos where everyone is fake and smiling. Other photos would be great but not too cheesy.

```html
<!DOCTYPE html>
<html lang="en">
<head>
<meta charset="utf-8">
<title>Trellowby- Marsh Vale — Developer Brochure</title>
<link href="https://fonts.googleapis.com/css2?family=Arimo:wght@400;700&display=swap" rel="stylesheet">
<style>
  :root {
    --brand-blue: #2b2f9e;
    --brand-red: #e3232c;
    --photo-light: #c9d6ea;
    --photo-mid: #7d95c4;
    --photo-dark: #2e3f86;
    --paper: #ffffff;
    --caption: #222222;
    --white: #ffffff;
  }
  * { margin: 0; padding: 0; box-sizing: border-box; }
  html, body {
    width: 900px; height: 1200px; overflow: hidden;
    background: var(--paper);
    font-family: "Arimo", Arial, sans-serif;
    color: var(--white);
  }
  .canvas { position: relative; width: 900px; height: 1200px; }

  .spread { position: absolute; left: 66px; width: 768px; height: 560px; display: flex; }
  .spread--outer { top: 6px; }
  .spread--inner { top: 610px; }
  .page { position: relative; width: 384px; height: 560px; overflow: hidden; }

  .photo { position: absolute; }
  .photo--tower { background: linear-gradient(135deg, var(--photo-light) 0%, var(--photo-mid) 45%, var(--photo-dark) 100%); }
  .photo--steel { background: linear-gradient(160deg, var(--photo-light) 0%, var(--photo-mid) 60%, var(--photo-dark) 100%); }
  .photo--site { background: linear-gradient(200deg, var(--photo-light) 0%, var(--photo-mid) 50%, var(--photo-dark) 100%); }

  .block { position: absolute; }
  .block--blue { background: var(--brand-blue); }
  .block--red { background: var(--brand-red); }

  .wordmark {
    position: absolute; display: flex; align-items: center; gap: 6px;
    color: var(--white); font-weight: 400; line-height: 1;
  }
  .wordmark__square { width: 12px; height: 12px; background: var(--white); flex: none; }
  .wordmark__name { font-size: 17px; }
  .wordmark--small .wordmark__name { font-size: 13px; }
  .wordmark--small .wordmark__square { width: 9px; height: 9px; }

  .caption { position: absolute; font-size: 13px; color: var(--caption); }

  /* back cover */
  .contact-band {
    position: absolute; left: 0; right: 0; bottom: 0; height: 44px;
    background: var(--brand-red);
    display: flex; flex-direction: column; justify-content: center; align-items: center;
    font-size: 6.5px; line-height: 1.35; text-align: center;
  }

  /* front cover */
  .cover-question {
    position: absolute; left: 186px; top: 228px; width: 198px; height: 216px;
    background: var(--brand-red);
    display: flex; align-items: center; justify-content: flex-end;
    padding: 0 12px 0 40px; text-align: right;
    font-size: 20px; font-weight: 400; line-height: 1.3;
  }

  /* inner pages */
  .headline { font-size: 20px; font-weight: 400; line-height: 1.1; color: var(--brand-red); margin-bottom: 6px; }
  .lead { font-size: 12px; line-height: 1.25; }
  .body-copy p { font-size: 7.6px; line-height: 1.4; margin-bottom: 8px; }
  .welcome { font-size: 12px; line-height: 1.3; }
  .invite { font-size: 10px; color: var(--brand-blue); margin-top: 8px; }
  .services__title { font-size: 10px; font-weight: 400; color: var(--brand-red); margin-bottom: 5px; }
  .services p { font-size: 7.4px; line-height: 1.4; margin-bottom: 5px; }
</style>
</head>
<body>
<div class="canvas">

  <section class="spread spread--outer">
    <article class="page page--back-cover">
      <div class="block block--blue" style="left:0;top:0;width:384px;height:516px;"></div>
      <div class="wordmark" style="left:124px;top:458px;">
        <span class="wordmark__square"></span>
        <span class="wordmark__name">Trellowby Marsh Vale</span>
      </div>
      <div class="contact-band">
        <span>Trellowby- Marsh Vale Conveyancing</span>
        <span>Level 4, 120 Harbour Lane, Marsh Vale VIC 3000</span>
        <span>Phone (03) 9000 1234 Fax (03) 9000 1235</span>
        <span>info@trellowby.com.au www.trellowby.com.au</span>
      </div>
    </article>

    <article class="page page--front-cover">
      <div class="photo photo--tower" role="img" aria-label="Glass high-rise office tower seen from below, toned blue" style="left:0;top:0;width:384px;height:560px;"></div>
      <h1 class="cover-question">Do property developers have a genuine alternative to high legal fees ?</h1>
      <div class="block block--blue" style="left:186px;top:444px;width:198px;height:40px;"></div>
      <div class="wordmark wordmark--small" style="left:236px;top:458px;">
        <span class="wordmark__square"></span>
        <span class="wordmark__name">Trellowby Marsh Vale</span>
      </div>
    </article>
  </section>
  <span class="caption" style="left:66px;top:578px;">Back Cover</span>
  <span class="caption" style="left:750px;top:578px;">Front Cover</span>

  <section class="spread spread--inner">
    <article class="page page--second">
      <div class="photo photo--steel" role="img" aria-label="Steel and glass roof structure, toned blue" style="left:0;top:0;width:384px;height:72px;"></div>
      <div class="photo photo--steel" role="img" aria-label="Edge of building facade, toned blue" style="left:334px;top:72px;width:50px;height:126px;"></div>
      <div class="block block--blue" style="left:0;top:72px;width:334px;height:126px;padding:8px 10px;">
        <h2 class="headline">100% of our developer<br>clients recommend us.</h2>
        <p class="lead">We already look after the conveyancing needs of more developers in victoria than any other conveyancing firm.</p>
      </div>
      <div class="block block--red body-copy" style="left:0;top:198px;width:384px;height:252px;padding:14px 12px;">
        <p>Industry benchmark off- the- plan contracts (tailored to the requirements of each development). Our special conditions (including variations, rebates and resale restrictions) are carefully chosen to protect the interests of our vendors while being commercially sensitive to ensure sales are not lost unnecessarily.</p>
        <p>Expert in guiding developers from first time dual occupancies to seasoned developers of large scale land and highrise projects.</p>
        <p>Our large team and highly refined systems ensure fastest possible settlement times after subdivision registration.</p>
        <p>We are available to train your project marketers on completing and executing contracts so that sales are not delayed or lost.</p>
        <p>Establishment of interest bearing trust accounts.</p>
        <p>Before you buy a development site have us thoroughly investigate the contract and vendors statement. We can then conduct the purchase settlement on your behalf.</p>
        <p>Highly experienced Conveyancers with the security of full Solicitor support.</p>
      </div>
      <div class="photo photo--steel" role="img" aria-label="Glass atrium roof grid seen from below, toned blue" style="left:0;top:450px;width:384px;height:110px;"></div>
    </article>

    <article class="page page--third">
      <div class="block block--blue" style="left:0;top:0;width:384px;height:86px;"></div>
      <div class="wordmark" style="left:196px;top:34px;">
        <span class="wordmark__square"></span>
        <span class="wordmark__name">Trellowby Marsh Vale</span>
      </div>
      <div class="block block--red" style="left:0;top:86px;width:384px;height:104px;padding:12px 20px;">
        <p class="welcome">We have the friendliest and most efficient staff. Every dealing you have with our dedicated Development Division will be prompt, professional and impressive. You will never need to follow us up!</p>
        <p class="invite">Please consider us next time you need Conveyancing.</p>
      </div>
      <div class="photo photo--site" role="img" aria-label="High-rise building under construction with crane, toned blue" style="left:0;top:190px;width:384px;height:236px;"></div>
      <div class="block block--blue services" style="left:0;top:426px;width:384px;height:134px;padding:10px 20px;">
        <h3 class="services__title">Services options:</h3>
        <p>Use us from contract preparation to settlement or;</p>
        <p>Have your Solicitor prepare the contract and use us as an alternative for the settlement stage only. Many Solicitors recommend us for this service already.</p>
        <p>Fast subdivision lodgements (including obtaining mortgagee's consent, Solicitor preparation of Land Titles Office application, owners corporation establishment).</p>
      </div>
    </article>
  </section>
  <span class="caption" style="left:66px;top:1176px;">2nd Page</span>
  <span class="caption" style="left:760px;top:1176px;">3th Page</span>

</div>
</body>
</html>
```